Bath Salt - Sachet Packet (5 Scents) Packaging Design

We sell products to professional salons in the USA. This product is used as the first step when treating clients to a pedicure spa. This product is called SALT SOAK (or Bath Salts). The salt is added to the water to cleanse the skin, create a pleasant fragrance, and change the color of the water.

This product has 5 different variations, based on the scent of the salt soak. The available scents are:
LAVENDER, MANDARIN, CUCUMBER-MELON, JASMINE, MINT.

We would like to see package designs for all 5 scents. The theme should be consistent across the different variations of scents. The design should focus on bright, attractive, floral colors/themes. The design should fully express the color and imagery that are associated with each scent. (Lavender scent should include purple colors, lavender flower, etc.). See example images for reference of popular designs/brands.

Ideal designs will incorporate a luxurious and premium aesthetic that combines elegant imagery, colors, and premium finishes. See example images for reference of popular designs/brands.

Each packet is individually sealed. See dimension artwork file for reference of the sachet packet size and layout.

See the attached document guidelines for more information about product name, key text, and brand logo.

Target Market(s)

Beauty & Nail Salons

Industry/Entity Type

Beauty

Font styles to use
Sans Serif
Script

Requirements
Must have
• Bright imagery and colors that relate to the target fragrance
Nice to have
• Premium and luxurious finishes (shiny accent, etc.)

```html
<!DOCTYPE html>
<html lang="en">
<head>
<meta charset="utf-8">
<title>Novea Mint Sea Salt Soak Sachet</title>
<link rel="stylesheet" href="https://fonts.googleapis.com/css2?family=Montserrat:wght@400;500;600;700&family=Great+Vibes&display=swap">
<style>
  :root {
    --page-bg: #ffffff;
    --seal-silver: #d7d9dc;
    --sheen-white: #f2f3f2;
    --mint-leaf: #56a82a;
    --mint-deep: #3f8a1c;
    --mint-dark: #2f6e14;
    --silver-text: #e4e5e6;
    --pill-silver: #cfd1d3;
    --pill-text: #3d3f42;
    --rule-silver: #dcdedf;
  }
  * { margin: 0; padding: 0; box-sizing: border-box; }
  html, body {
    width: 797px; height: 1200px; overflow: hidden;
    background: var(--page-bg);
  }
  .canvas { position: relative; width: 797px; height: 1200px; }
  .sachet {
    position: absolute; left: 81px; top: 120px;
    width: 632px; height: 962px;
    border-radius: 30px 30px 6px 6px;
    overflow: hidden;
    background: linear-gradient(180deg, var(--sheen-white) 0%, var(--sheen-white) 38%, #b9d8a0 46%, var(--mint-leaf) 56%, var(--mint-deep) 78%, var(--mint-leaf) 100%);
    box-shadow: inset 0 0 0 14px rgba(215,217,220,0.55);
    font-family: "Montserrat", sans-serif;
    color: var(--silver-text);
    text-align: center;
  }
  .mint-photo {
    position: absolute; left: 0; top: 0; width: 632px; height: 360px;
    background: radial-gradient(ellipse at 55% 45%, #5fb733 0%, #4a9a25 45%, rgba(90,170,50,0.5) 70%, rgba(242,243,242,0) 100%);
  }
  .brand {
    position: absolute; left: 0; right: 0; top: 388px;
    font-size: 98px; font-weight: 500; letter-spacing: 2px; line-height: 1;
  }
  .brand-tagline {
    position: absolute; left: 0; right: 0; top: 500px;
    padding-left: 170px;
    font-size: 17px; font-weight: 400; letter-spacing: 5px;
  }
  .range-pill {
    position: absolute; left: 107px; top: 545px; width: 416px; height: 35px;
    border-radius: 18px;
    background: linear-gradient(90deg, #a9acaf, var(--pill-silver) 30%, #f0f1f2 60%, #b5b8bb);
    color: var(--pill-text);
    font-size: 22px; font-weight: 700; letter-spacing: 1.5px; line-height: 35px;
  }
  .scent {
    position: absolute; left: 0; right: 0; top: 598px;
    font-size: 66px; font-weight: 500; letter-spacing: 3px; line-height: 1;
  }
  .scent-fr {
    position: absolute; left: 0; right: 0; top: 668px;
    font-family: "Great Vibes", cursive; font-size: 50px; line-height: 1;
  }
  .rule { position: absolute; height: 2px; background: var(--rule-silver); }
  .rule-top { left: 87px; width: 456px; top: 746px; }
  .rule-bottom { left: 125px; width: 382px; top: 836px; }
  .product {
    position: absolute; left: 0; right: 0; top: 760px;
    font-size: 33px; font-weight: 600; letter-spacing: 1px; line-height: 1.2;
  }
  .product-fr {
    position: absolute; left: 0; right: 0; top: 806px;
    font-size: 20px; font-weight: 400;
  }
  .net-weight {
    position: absolute; left: 0; right: 0; top: 856px;
    font-size: 15px; font-weight: 500; word-spacing: 3px;
  }
</style>
</head>
<body>
<div class="canvas">
  <div class="sachet">
    <div class="mint-photo" role="img" aria-label="Photo of a bunch of fresh mint leaves"></div>
    <div class="brand">Novea</div>
    <div class="brand-tagline">BEAUTY &amp; SPA</div>
    <div class="range-pill">DELUX PEDICURE SPA</div>
    <div class="scent">MINT</div>
    <div class="scent-fr">Menthe</div>
    <div class="rule rule-top"></div>
    <div class="product">SEA SALT SOAK</div>
    <div class="product-fr">Sel de mer trempé</div>
    <div class="rule rule-bottom"></div>
    <div class="net-weight">net wt. &nbsp;| &nbsp;poids net &nbsp;/ &nbsp;12 oz. &nbsp;| &nbsp;35 g ℮</div>
  </div>
</div>
</body>
</html>
```